依頼詳細
■入れてほしい文言
エクセルデータ参照してください

■ のぼり、ポスターサイズ情報
サイズ:横600mm×縦1800mm以内

■ デザインへの要望
洋風調、和風調 のぼりデザインを作成したい
デザイン参考に添付ファイルの画像を参照
記載項目
サイズ:横600mm×縦1800mm以内
希望イメージ
シンプル 複雑
単色 カラフル
暗い 明るい
日常 高級
遊び心 厳粛
未来的 伝統的
女性的 男性的
希望する色
納品ファイル
• イラストレーター形式 (.ai)
• フォトショップ形式 (.psd)
• PNG形式 (.png)
補足説明

```html
<!DOCTYPE html>
<html lang="ja">
<head>
<meta charset="utf-8">
<title>山辺建具 のぼり</title>
<link rel="stylesheet" href="https://fonts.googleapis.com/css2?family=Noto+Serif+JP:wght@400;500;700;900&display=swap">
<style>
  :root {
    --ink: #111111;
    --white: #ffffff;
    --gold: #b99466;
    --gold-light: #cdaa7c;
    --gold-deep: #9c774c;
    --red: #7c1c19;
    --red-mid: #6a1714;
    --red-dark: #3a0a09;
    --night: #120404;
    --wood-light: #e9b27a;
    --wood-mid: #c98a4e;
    --wood-shade: #8a5a30;
    --wood-dark: #2a1a10;
  }
  * { margin: 0; padding: 0; box-sizing: border-box; }
  html, body { width: 1200px; height: 3492px; overflow: hidden; background: var(--night); }
  .banner {
    position: relative;
    width: 1200px;
    height: 3492px;
    overflow: hidden;
    font-family: "Noto Serif JP", serif;
  }
  .field-top {
    position: absolute; left: 0; top: 0; width: 1200px; height: 1200px;
    background: linear-gradient(180deg, var(--night) 0%, var(--red-dark) 25%, var(--red) 60%, var(--red-mid) 85%, var(--red-dark) 100%);
  }
  .field-bottom {
    position: absolute; left: 0; top: 1985px; width: 1200px; height: 1507px;
    background: linear-gradient(180deg, var(--red-dark) 0%, var(--red) 35%, var(--red-mid) 70%, var(--night) 100%);
  }
  .lattice-photo {
    position: absolute; left: 0; top: 1200px; width: 1200px; height: 785px;
    background: radial-gradient(ellipse at 50% 45%, var(--wood-light) 0%, var(--wood-mid) 55%, var(--wood-shade) 85%, var(--wood-dark) 100%);
  }
  .band { position: absolute; width: 180px; }
  .band-top {
    left: 220px; top: 0; height: 1100px;
    background: linear-gradient(180deg, var(--white) 0%, var(--white) 82%, rgba(255,255,255,0) 100%);
  }
  .band-bottom {
    left: 830px; top: 2150px; height: 1342px;
    background: linear-gradient(180deg, rgba(255,255,255,0) 0%, var(--white) 24%, var(--white) 100%);
  }
  .vertical {
    position: absolute;
    writing-mode: vertical-rl;
    text-orientation: upright;
    line-height: 1;
  }
  .tagline {
    left: 240px; top: 100px;
    font-size: 140px; font-weight: 500; letter-spacing: 12px;
    color: var(--ink);
  }
  .union-name {
    left: 850px; top: 2620px;
    font-size: 138px; font-weight: 500; letter-spacing: 0;
    color: var(--ink);
  }
  .title {
    font-weight: 400;
    background: linear-gradient(180deg, var(--gold-light), var(--gold-deep));
    -webkit-background-clip: text; background-clip: text;
    -webkit-text-fill-color: transparent;
    color: var(--gold);
  }
  .title-place {
    left: 715px; top: 150px;
    font-size: 440px; letter-spacing: 30px;
  }
  .title-craft {
    left: 30px; top: 2060px;
    font-size: 460px; letter-spacing: 20px;
  }
  .roman {
    position: absolute;
    color: var(--white);
    font-weight: 700;
    line-height: 1;
    white-space: nowrap;
  }
  .roman-place { left: 50px; top: 1070px; font-size: 104px; letter-spacing: 2px; }
  .roman-craft { left: 520px; top: 2030px; font-size: 124px; letter-spacing: 2px; }
</style>
</head>
<body>
  <main class="banner">
    <div class="field-top" role="img" aria-label="暗い赤のグラデーション地に幾何学文様"></div>
    <div class="lattice-photo" role="img" aria-label="木製組子細工の建具の写真"></div>
    <div class="field-bottom" role="img" aria-label="暗い赤のグラデーション地に幾何学文様"></div>

    <div class="band band-top"></div>
    <div class="band band-bottom"></div>

    <p class="vertical tagline">山里の小京都</p>
    <h1 class="vertical title title-place">山辺</h1>
    <p class="roman roman-place">YAMABE</p>

    <p class="roman roman-craft">TATEGU</p>
    <h2 class="vertical title title-craft">建具</h2>
    <p class="vertical union-name">山辺建具組合</p>
  </main>
</body>
</html>
```